Want a package created for a new protein bar

We would like a new package created for a new protein bar project The name of the bar will be VOLMBite a real food protein bar, we would like a ‘window’ on the package of bar like Brave Meadow bar below in images.

VOLMBite
‘Super Food Bar’
14g of Whey Protein
The package film size is the following 12cm width x 15cm Length,
Flavor Peanut Chocolate Chip, additional information will be attached shortly like nutrition facts,

Target Market(s)

fitness market, bodybuilders, athletes, everyday people

Industry/Entity Type

Health Product

Logo Text

VOLMBite

Font styles to use
Serif
Sans Serif
Decorative

Requirements
Must have
• Package window

```html
<!DOCTYPE html>
<html lang="en">
<head>
<meta charset="utf-8">
<title>VOLMBite Super Food Bar – Wrapper</title>
<link rel="stylesheet" href="https://fonts.googleapis.com/css2?family=Anton&family=Oswald:wght@600;700&display=swap">
<style>
  :root {
    --paper: #ffffff;
    --sky-light: #bfeef7;
    --sky: #35c6ec;
    --sky-deep: #1489c9;
    --ink: #0b0b0b;
    --sun: #fff200;
    --cocoa: #6b3318;
    --cocoa-deep: #4a2110;
    --flame: #e4481d;
    --cream: #ffffff;
    --steel: #7d7d7d;
  }
  * { margin: 0; padding: 0; box-sizing: border-box; }
  html, body { width: 1200px; height: 481px; overflow: hidden; background: var(--paper); }
  .wrapper {
    position: relative;
    width: 1200px;
    height: 481px;
    overflow: hidden;
    background: var(--paper);
    font-family: "Anton", "Oswald", sans-serif;
  }
  .backdrop { position: absolute; inset: 0; }
  .brand-name {
    position: absolute;
    left: 196px; top: 64px;
    font-family: "Anton", sans-serif;
    font-size: 58px;
    line-height: 1;
    color: var(--ink);
    letter-spacing: 1px;
  }
  .headline-super {
    position: absolute;
    left: 92px; top: 160px;
    font-family: "Anton", sans-serif;
    font-size: 112px;
    line-height: 1;
    color: var(--sun);
    -webkit-text-stroke: 6px var(--cocoa);
    paint-order: stroke fill;
    letter-spacing: -1px;
  }
  .headline-foodbar {
    position: absolute;
    left: 406px; top: 170px;
    font-family: "Anton", sans-serif;
    font-size: 60px;
    line-height: 1;
    color: var(--sun);
    -webkit-text-stroke: 5px var(--cocoa);
    paint-order: stroke fill;
  }
  .flavor {
    position: absolute;
    left: 108px; top: 296px;
    font-family: "Oswald", sans-serif;
    font-weight: 700;
    font-size: 22px;
    line-height: 1;
    color: var(--flame);
    letter-spacing: 0.2px;
  }
  .protein-banner {
    position: absolute;
    left: 508px; top: 240px;
    width: 204px; height: 94px;
    background: var(--cocoa);
    clip-path: polygon(0 0, 100% 0, 93% 100%, 0 100%);
  }
  .protein-text {
    position: absolute;
    left: 540px; top: 246px;
    font-family: "Oswald", sans-serif;
    font-weight: 700;
    color: var(--cream);
    line-height: 1;
    text-align: center;
  }
  .protein-text .of-whey { display: block; font-size: 27px; }
  .protein-text .protein { display: block; font-size: 36px; margin-top: 8px; }
  .protein-badge {
    position: absolute;
    left: 406px; top: 228px;
    width: 118px; height: 118px;
    border-radius: 50%;
    background: var(--cocoa);
    border: 3px solid var(--cocoa-deep);
    display: flex; align-items: center; justify-content: center;
  }
  .protein-badge::before {
    content: "";
    position: absolute;
    inset: 8px;
    border-radius: 50%;
    border: 2px solid var(--sky);
  }
  .protein-amount {
    font-family: "Oswald", sans-serif;
    font-weight: 700;
    font-size: 44px;
    color: var(--cream);
    line-height: 1;
  }
  .net-weight {
    position: absolute;
    left: 1116px; top: 398px;
    font-family: "Oswald", sans-serif;
    font-weight: 700;
    font-size: 40px;
    color: var(--steel);
    line-height: 1;
  }
</style>
</head>
<body>
<main class="wrapper">
  <svg class="backdrop" width="1200" height="481" viewBox="0 0 1200 481" aria-hidden="true">
    <defs>
      <linearGradient id="panel-glow" x1="0" y1="0" x2="1" y2="1">
        <stop offset="0" stop-color="#f4fbf0"/>
        <stop offset="0.35" stop-color="var(--sky-light)"/>
        <stop offset="1" stop-color="var(--sky)"/>
      </linearGradient>
      <linearGradient id="panel-core" x1="0" y1="0.3" x2="1" y2="0.7">
        <stop offset="0" stop-color="#c9f3fb"/>
        <stop offset="0.4" stop-color="var(--sky)"/>
        <stop offset="1" stop-color="var(--sky-deep)"/>
      </linearGradient>
    </defs>
    <polygon class="panel-outer" points="0,0 780,0 780,481 0,481" fill="url(#panel-glow)"/>
    <polygon class="panel-core" points="28,232 150,28 780,28 780,481 120,481" fill="url(#panel-core)"/>
    <polygon class="panel-facet" points="150,28 520,28 300,250 28,232" fill="#ffffff" opacity="0.18"/>
  </svg>

  <div class="brand-name">VOLMBite</div>

  <div class="headline-super">SUPER</div>
  <div class="headline-foodbar">FOOD BAR</div>
  <div class="flavor">PEANUT CHOCOLATE CHIP</div>

  <div class="protein-banner"></div>
  <div class="protein-text"><span class="of-whey">OF WHEY</span><span class="protein">PROTEIN</span></div>
  <div class="protein-badge"><span class="protein-amount">14g</span></div>

  <svg class="splash-art" style="position:absolute;left:500px;top:0" width="410" height="481" viewBox="0 0 410 481" role="img" aria-label="Illustration of a swirling chocolate and peanut butter splash with peanuts and an open peanut shell">
    <defs>
      <linearGradient id="choco-swirl" x1="0" y1="0" x2="1" y2="0">
        <stop offset="0" stop-color="#5a2a14"/>
        <stop offset="0.5" stop-color="#8a4a22"/>
        <stop offset="1" stop-color="#d99a4e"/>
      </linearGradient>
    </defs>
    <path d="M150,0 C300,20 390,120 390,260 C390,390 310,460 270,481 L20,481 C60,450 150,430 210,360 C270,280 260,140 200,60 C180,35 160,15 150,0 Z" fill="url(#choco-swirl)"/>
  </svg>

  <svg class="milk-art" style="position:absolute;left:1045px;top:241px" width="155" height="240" viewBox="0 0 155 240" role="img" aria-label="Illustration of a white milk splash">
    <defs>
      <linearGradient id="milk-tone" x1="0" y1="0" x2="1" y2="1">
        <stop offset="0" stop-color="#e6e6e6"/>
        <stop offset="1" stop-color="#bdbdbd"/>
      </linearGradient>
    </defs>
    <path d="M155,20 C110,40 70,90 50,150 C40,190 30,220 20,240 L155,240 Z" fill="url(#milk-tone)"/>
  </svg>

  <div class="net-weight">64g</div>
</main>
</body>
</html>
```